Option Sheet

We need a one page option sheet with a left to right reading of the five options. It should be a one sheet, multiple colors and definitive separations between options This is used in a sales consultation. Backround or colors not in option need to have the follow RGB value (5 red, 20 green, 63 blue)

We added a smaller text file, please change that point

Target Market(s)

Divorce

Industry/Entity Type

Legal

Requirements
Must have
• 1) All five options left to right
• 2)language included in sheet

```html
<!DOCTYPE html>
<html lang="en">
<head>
<meta charset="UTF-8">
<title>Five Options – Divorce</title>
<link href="https://fonts.googleapis.com/css2?family=Bebas+Neue&family=Open+Sans:wght@400;600;700&display=swap" rel="stylesheet">
<style>
  :root {
    --bg: #d5d6d8;
    --ink: #555658;
    --text: #3f4042;
    --card: #ffffff;
    --blue: #4b78bd;
    --orange: #f8ad3e;
    --purple: #7458a6;
    --red: #ef5b46;
    --teal: #45bea7;
  }
  * { margin: 0; padding: 0; box-sizing: border-box; }
  html, body { width: 1200px; height: 849px; overflow: hidden; background: var(--bg); }
  .sheet { position: relative; width: 1200px; height: 849px; font-family: "Open Sans", Arial, sans-serif; color: var(--text); }
  .sheet-title {
    position: absolute; top: 50px; left: 0; width: 1200px; text-align: center;
    font-family: "Bebas Neue", "Arial Narrow", sans-serif; font-weight: 400;
    font-size: 66px; letter-spacing: 2px; color: var(--ink); line-height: 1;
  }
  .title-rule { position: absolute; top: 125px; left: 205px; }
  .option { position: absolute; top: 182px; width: 191px; --accent: var(--blue); }
  .option--1 { left: 76px; --accent: var(--blue); }
  .option--2 { left: 289px; --accent: var(--orange); }
  .option--3 { left: 503px; --accent: var(--purple); }
  .option--4 { left: 717px; --accent: var(--red); }
  .option--5 { left: 932px; --accent: var(--teal); }
  .option-label {
    height: 55px; text-align: center; color: var(--accent);
    font-family: "Bebas Neue", "Arial Narrow", sans-serif; font-size: 31px; letter-spacing: 0.5px; line-height: 40px;
  }
  .option-head {
    height: 88px; background: var(--accent); color: #fff;
    display: flex; align-items: center; justify-content: center; text-align: center;
    font-size: 20px; font-weight: 600; line-height: 1.25; padding: 0 10px;
    box-shadow: 3px 5px 8px rgba(0,0,0,0.22); position: relative; z-index: 1;
  }
  .card {
    background: var(--card); padding: 12px 12px 10px 10px;
    box-shadow: 3px 5px 8px rgba(0,0,0,0.22); position: relative;
  }
  .card--pros { height: 140px; }
  .option--5 .card--pros { height: 259px; }
  .card--cons { margin-top: 21px; height: 301px; }
  .option--5 .card--cons { margin-top: 23px; height: 180px; }
  .card--cons::after {
    content: ""; position: absolute; left: 0; right: 0; bottom: 0; height: 32px; background: var(--accent);
  }
  .card-heading { color: var(--accent); font-size: 18.5px; font-weight: 700; margin-bottom: 10px; }
  .card-list { list-style: none; font-size: 12px; line-height: 1.32; }
  .card-list li { margin-bottom: 11px; }
  .card--cons .card-list li { margin-bottom: 9px; }
</style>
</head>
<body>
<main class="sheet">
  <h1 class="sheet-title">Five Options – Divorce</h1>
  <svg class="title-rule" width="790" height="20" viewBox="0 0 790 20" aria-hidden="true">
    <line x1="10" y1="10" x2="780" y2="10" stroke="#3a3b3d" stroke-width="2"/>
    <circle cx="10" cy="10" r="8" fill="#3a3b3d"/>
    <circle cx="780" cy="10" r="8" fill="#3a3b3d"/>
  </svg>

  <section class="option option--1">
    <div class="option-label">Option 1</div>
    <div class="option-head">Do Nothing</div>
    <div class="card card--pros">
      <h2 class="card-heading">Advantages:</h2>
      <ul class="card-list"><li>Stay married</li><li>No life Changes</li></ul>
    </div>
    <div class="card card--cons">
      <h2 class="card-heading">Disadvantages:</h2>
      <ul class="card-list">
        <li>Remain unhappy, depressed, anxious.</li>
        <li>Money and assets may disappear.</li>
        <li>What is going to change?</li>
      </ul>
    </div>
  </section>

  <section class="option option--2">
    <div class="option-label">Option 2</div>
    <div class="option-head">Go to<br>Counseling</div>
    <div class="card card--pros">
      <h2 class="card-heading">Advantages:</h2>
      <ul class="card-list"><li>Reconcile marriage</li><li>Help make a better life</li></ul>
    </div>
    <div class="card card--cons">
      <h2 class="card-heading">Disadvantages:</h2>
      <ul class="card-list">
        <li>Past issues are highlighted and may drudge up old wounds.</li>
        <li>It may just clarify the reasons you need to separate and/or divorce.</li>
        <li>Both parties must be invested and willing to participate.</li>
      </ul>
    </div>
  </section>

  <section class="option option--3">
    <div class="option-label">Option 3</div>
    <div class="option-head">Do it Yourself</div>
    <div class="card card--pros">
      <h2 class="card-heading">Advantages:</h2>
      <ul class="card-list"><li>No attorney fees</li><li>You are your on attorney</li></ul>
    </div>
    <div class="card card--cons">
      <h2 class="card-heading">Disadvantages:</h2>
      <ul class="card-list">
        <li>People often find that what is “fair,” may in fact, not be truly fair.</li>
        <li>Often times, people do not know the risks.</li>
        <li>Complicated legal system within intrigue rules.</li>
        <li>Unsure how to complete the necessary paperwork and meet the deadlines.</li>
      </ul>
    </div>
  </section>

  <section class="option option--4">
    <div class="option-label">Option 4</div>
    <div class="option-head">Limited<br>Representation</div>
    <div class="card card--pros">
      <h2 class="card-heading">Advantages:</h2>
      <ul class="card-list"><li>Balance between going alone</li><li>and our limited involvement in the case</li></ul>
    </div>
    <div class="card card--cons">
      <h2 class="card-heading">Disadvantages:</h2>
      <ul class="card-list">
        <li>Our terms may not benefit from our legal knowledge.</li>
        <li>The legal consequences of your legal documents will not be explained to you so that you can formulate a plan for handling the rest of your case.</li>
        <li>Your spouse or other parties may cause your legal fees to increase significantly without action on your part.</li>
      </ul>
    </div>
  </section>

  <section class="option option--5">
    <div class="option-label">Option 5</div>
    <div class="option-head">Hire Us</div>
    <div class="card card--pros">
      <h2 class="card-heading">Advantages:</h2>
      <ul class="card-list">
        <li>Gain the full benefits of our experience</li>
        <li>Have a team of Family Law focus attorneys</li>
        <li>Often saves you or makes you money in the long run</li>
        <li>Save you time, energy and stress</li>
      </ul>
    </div>
    <div class="card card--cons">
      <h2 class="card-heading">Disadvantages:</h2>
      <ul class="card-list"><li>Initial cost</li></ul>
    </div>
  </section>
</main>
</body>
</html>
```